Need a banner designed to help prank my neighbor.

I'm looking for creativity and fun in a banner that I will hang on a large tree outside my house facing a neighbor. He just started decorating for Christmas and I always joke with him that it is too early. This is a fun project. Nothing too serious. I welcome your skills to make it awesome.

I have the basics of a sign designed (attached), but I need it brought to the next level with better font and images.

Banner will be printed at 4-feet x 8-feet.
Top part of my mock up is most important to see/read easily.

```html
<!DOCTYPE html>
<html lang="en">
<head>
<meta charset="UTF-8">
<title>Thanksgiving First Banner</title>
<link rel="stylesheet" href="https://fonts.googleapis.com/css2?family=Bebas+Neue&family=Montserrat:wght@500&family=Roboto+Condensed:wght@700&display=swap">
<style>
  :root {
    --stop-red: #e2001a;
    --banner-red: #e5191b;
    --banner-green: #246424;
    --paper: #ffffff;
    --turkey-brown: #7a3a1c;
    --turkey-light: #a65a2e;
    --antler-line: #dfe9df;
  }
  html, body {
    margin: 0;
    padding: 0;
    overflow: hidden;
    background: var(--paper);
  }
  .banner {
    position: relative;
    width: 1200px;
    height: 600px;
    background: var(--paper);
    overflow: hidden;
  }
  .stop-sign {
    position: absolute;
    left: 22px;
    top: 27px;
    width: 172px;
    height: 172px;
  }
  .stop-sign text {
    font-family: "Roboto Condensed", "Arial Narrow", sans-serif;
    font-weight: 700;
  }
  .headline {
    position: absolute;
    left: 206px;
    top: 46px;
    width: 980px;
    margin: 0;
    font-family: "Bebas Neue", Impact, sans-serif;
    font-weight: 400;
    font-size: 104px;
    line-height: 1;
    color: var(--stop-red);
    white-space: nowrap;
    transform: scaleX(0.8);
    transform-origin: left center;
    letter-spacing: 0;
  }
  .band-red {
    position: absolute;
    left: 18px;
    top: 222px;
    width: 1164px;
    height: 150px;
    background: var(--banner-red);
  }
  .band-red .subhead {
    margin: 0;
    position: absolute;
    left: 0;
    right: 0;
    top: 44px;
    text-align: center;
    font-family: "Bebas Neue", Impact, sans-serif;
    font-weight: 400;
    font-size: 74px;
    line-height: 1;
    color: var(--paper);
  }
  .band-green {
    position: absolute;
    left: 18px;
    top: 372px;
    width: 1164px;
    height: 210px;
    background: var(--banner-green);
  }
  .hashtags {
    list-style: none;
    margin: 0;
    padding: 0;
    position: absolute;
    left: 0;
    right: 0;
    top: 22px;
    text-align: center;
    font-family: "Montserrat", Arial, sans-serif;
    font-weight: 500;
    font-size: 40px;
    line-height: 58px;
    color: var(--paper);
  }
  .reindeer {
    position: absolute;
    top: 112px;
    width: 64px;
    height: 76px;
    border-radius: 32px 32px 30px 30px;
    background: linear-gradient(180deg, rgba(223,233,223,0.25), rgba(223,233,223,0.1));
    border: 2px solid var(--antler-line);
  }
  .reindeer-left { left: 227px; }
  .reindeer-right { left: 887px; }
  .turkey {
    position: absolute;
    left: 1028px;
    top: 186px;
    width: 172px;
    height: 200px;
    border-radius: 90px 0 0 90px;
    background: radial-gradient(circle at 70% 50%, var(--turkey-light), var(--turkey-brown));
  }
</style>
</head>
<body>
  <main class="banner">
    <svg class="stop-sign" viewBox="0 0 172 172" aria-label="Stop sign">
      <polygon points="50,0 122,0 172,50 172,122 122,172 50,172 0,122 0,50" fill="#ffffff" stroke="#2a2a2a" stroke-width="3"/>
      <polygon points="53,8 119,8 164,53 164,119 119,164 53,164 8,119 8,53" fill="var(--stop-red)"/>
      <text x="86" y="108" text-anchor="middle" font-size="56" fill="#ffffff">STOP</text>
    </svg>
    <h1 class="headline">Premature Christmas Decorating!</h1>

    <section class="band-red">
      <h2 class="subhead">Thanksgiving First!</h2>
    </section>

    <section class="band-green">
      <ul class="hashtags">
        <li>#LightsGoUpAfterThanksgiving</li>
        <li>#SaveTheBabyReindeer</li>
        <li>#LookingAtYou4281</li>
      </ul>
      <div class="reindeer reindeer-left" role="img" aria-label="Outlined reindeer head icon"></div>
      <div class="reindeer reindeer-right" role="img" aria-label="Outlined reindeer head icon"></div>
    </section>

    <div class="turkey" role="img" aria-label="Cartoon turkey in a pilgrim hat peeking around the banner edge"></div>
  </main>
</body>
</html>
```